Business Card & Logo Design - Hedge Fund

We need a business card and logo design for a hedge fund. The hedge fund is named Morvane Equity LLC. Morvane Equity was created by finance professors and the strategy is based academic research that looks for patterns in stock prices. The design should look conservative, solid, strong. We favor a classic style - nothing flashy. The logo can relate to the name Morvane Equity, or it could involve a symbol design that connotes "science" . We are open to ideas. We do not want alot of colors - but if any, color - blue is preferred. The font that seems to look best for the name (Morvane Equity) is arial black. We are open to ideas. Most important - we want to see a mock up of an actual business card with the logo concept embedded. The business card should include space for : company name, individual name, position title, cell phone, address. We hope to have this work done by Sept. 8.

Target Market(s)

We will be meeting with and giving the business card to institutions and high net worth individuals.

Industry/Entity Type

Investment Advisory

Contact Information for Business Card

Company name - Morvane Equity LLC
Individual name - Peter Dalby
Title - Portfolio Manager
Cell - (412) 555-0187
Address - 2650 Birchmont Lane, Suite 300, Atlanta GA 30327

Font styles to use
Other font styles liked:
• Arial

Colors
3277b5
0255a3
85acd3
cedeed
fdf9cf
d9d9d9
e6e6e6
f04a50
6b449b

Requirements
Must have
• Must have card details that are sited above.
• We would like a logo related to the name (Morvane Equity) or concept of the fund.
Nice to have
• We want conservative / understated / clean crisp look.
• If any colors - we prefer conservative appearance - blue / gray.
• I have enclosed an example of a card style that looks attractive - please do not exactly copy this card. This is not our company or logo. I feel the layout is attractive - just as an example
Should not have
• Avoid too much color.
• I have selected some preferred colors. Please do not use all of the colors - I have selected a few that might work - but I am not sure. We are open to your ideas so please do not feel the need to use all or any of these.

```html
<!DOCTYPE html>
<html lang="en">
<head>
<meta charset="utf-8">
<title>Morvane Equity LLC — Business Card</title>
<link rel="stylesheet" href="https://fonts.googleapis.com/css2?family=Roboto:wght@400;500;700&display=swap">
<style>
  :root {
    --backdrop: #1b1b1b;
    --card: #232323;
    --card-edge: #2c2c2c;
    --ink: #f2f2f2;
    --silver: #d9d9d9;
    --blue: #3a9fd0;
    --rule: #8a8a8a;
  }
  * { margin: 0; padding: 0; box-sizing: border-box; }
  html, body {
    width: 1200px; height: 1200px; overflow: hidden;
    background: var(--backdrop);
    font-family: "Roboto", Arial, sans-serif;
  }
  .canvas {
    position: relative; width: 1200px; height: 1200px;
  }
  .card {
    position: absolute; left: 180px;
    width: 840px; height: 480px;
    background: var(--card);
    border: 1px solid var(--card-edge);
    border-radius: 22px;
    box-shadow: 0 18px 40px rgba(0,0,0,.55);
  }
  .card--back { top: 70px; }
  .card--front { top: 650px; }

  /* Back */
  .back-brand {
    position: absolute; inset: 0;
    display: flex; flex-direction: column; align-items: center; justify-content: center;
    color: var(--silver); font-weight: 700;
  }
  .back-brand .brand-name { font-size: 58px; letter-spacing: 4px; line-height: 1; }
  .back-brand .brand-sub { font-size: 26px; letter-spacing: 6px; margin-top: 10px; }

  /* Front */
  .front-brand {
    position: absolute; left: 56px; top: 52px;
    color: var(--blue); font-weight: 700;
  }
  .front-brand .brand-name { font-size: 50px; letter-spacing: 3px; line-height: 1; }
  .front-brand .brand-sub { font-size: 24px; letter-spacing: 5px; margin-top: 6px; }

  .person {
    position: absolute; left: 56px; top: 268px;
    display: flex; align-items: baseline; gap: 10px;
  }
  .person-name { color: var(--ink); font-size: 38px; font-weight: 500; }
  .person-title { color: var(--blue); font-size: 24px; font-weight: 500; }

  .divider {
    position: absolute; left: 56px; right: 56px; top: 326px;
    height: 1px; background: var(--rule);
  }

  .contacts {
    position: absolute; left: 56px; top: 342px;
    list-style: none; color: var(--ink); font-size: 21px;
  }
  .contacts li { display: flex; align-items: center; gap: 14px; height: 34px; }
  .contacts svg { width: 20px; height: 20px; fill: var(--blue); }

  .address {
    position: absolute; right: 56px; top: 346px;
    text-align: right; color: var(--ink); font-size: 22px; line-height: 34px;
    font-style: normal;
  }
</style>
</head>
<body>
<main class="canvas">

  <section class="card card--back" aria-label="Card back">
    <div class="back-brand">
      <span class="brand-name">MORVANE</span>
      <span class="brand-sub">EQUITY LLC</span>
    </div>
  </section>

  <section class="card card--front" aria-label="Card front">
    <div class="front-brand">
      <div class="brand-name">MORVANE</div>
      <div class="brand-sub">EQUITY LLC</div>
    </div>

    <div class="person">
      <span class="person-name">Peter Dalby</span>
      <span class="person-title">/ Portfolio Manager</span>
    </div>

    <div class="divider"></div>

    <ul class="contacts">
      <li>
        <svg viewBox="0 0 24 24" aria-hidden="true"><path d="M6.6 10.8a15.1 15.1 0 0 0 6.6 6.6l2.2-2.2a1 1 0 0 1 1-.25 11.4 11.4 0 0 0 3.6.57 1 1 0 0 1 1 1V20a1 1 0 0 1-1 1A17 17 0 0 1 3 4a1 1 0 0 1 1-1h3.5a1 1 0 0 1 1 1c0 1.25.2 2.45.57 3.57a1 1 0 0 1-.25 1z"/></svg>
        <span>(412) 555-0187</span>
      </li>
      <li>
        <svg viewBox="0 0 24 24" aria-hidden="true"><path d="M2 5h20v14H2z M3.5 6.5 12 13l8.5-6.5" fill="none" stroke="#3a9fd0" stroke-width="2"/></svg>
        <span>info@morvaneequity.com</span>
      </li>
    </ul>

    <address class="address">
      2650 Birchmont Lane, Suite 300<br>
      Atlanta GA 30327
    </address>
  </section>

</main>
</body>
</html>
```